Book cover for book about Climate Change

Looking for a clean, bold, and attractive cover for a mass-market paperback (5.5"x 8.5") about solving the climate change problem. Title is either "Where the Rivers Begin” or A Garden Left Standing” (your choice), subtitle is "A five-step plan to reverse climate change — to ensure that your grandchildren will live on a clean and comfortable planet," author is Milo Pardrey. Thinking that it *might* feature an image of Earth (or a portion thereof) and its very thin layer of atmosphere -- but STRONGLY encourage other ideas too!

Requirements
Nice to have
• Keep it positive — NOT scary doom-and-gloom

```html
<!DOCTYPE html>
<html lang="en">
<head>
<meta charset="utf-8">
<title>A Garden Left Standing — Milo Pardrey</title>
<link href="https://fonts.googleapis.com/css2?family=Comfortaa:wght@300;700&family=Jost:wght@500&display=swap" rel="stylesheet">
<style>
  :root {
    --cover-orange: #ff9214;
    --title-navy: #172872;
    --subtitle-white: #ffffff;
    --ocean-deep: #0f2a66;
    --ocean-mid: #2a4f8f;
    --cloud-white: #e9eef3;
    --land-green: #3f7a3a;
  }
  * { margin: 0; padding: 0; box-sizing: border-box; }
  html, body {
    width: 776px;
    height: 1200px;
    overflow: hidden;
    background: var(--cover-orange);
  }
  .cover {
    position: relative;
    width: 776px;
    height: 1200px;
    background: var(--cover-orange);
    overflow: hidden;
  }
  .earth {
    position: absolute;
    top: 0;
    left: 0;
    width: 776px;
    height: 1200px;
  }
  .title {
    position: absolute;
    left: 66px;
    top: 212px;
    font-family: "Jost", sans-serif;
    font-weight: 500;
    color: var(--title-navy);
    font-size: 124px;
    line-height: 159px;
    letter-spacing: 2px;
  }
  .title span { display: block; }
  .subtitle {
    position: absolute;
    left: 78px;
    top: 850px;
    width: 560px;
    font-family: "Comfortaa", sans-serif;
    font-weight: 300;
    font-size: 29px;
    line-height: 45px;
    color: var(--subtitle-white);
  }
  .subtitle strong { font-weight: 700; }
  .author {
    position: absolute;
    left: 0;
    width: 776px;
    top: 1110px;
    text-align: center;
    font-family: "Jost", sans-serif;
    font-weight: 500;
    font-size: 27px;
    letter-spacing: 17px;
    color: var(--title-navy);
    padding-left: 10px;
  }
</style>
</head>
<body>
<main class="cover">
  <svg class="earth" viewBox="0 0 776 1200" role="img" aria-label="Photograph of planet Earth seen from space: blue oceans, swirling white clouds and green continents in the top-right corner">
    <defs>
      <radialGradient id="earth-tones" cx="0.62" cy="0.45" r="0.55">
        <stop offset="0" stop-color="var(--land-green)"/>
        <stop offset="0.35" stop-color="var(--ocean-mid)"/>
        <stop offset="0.7" stop-color="var(--ocean-deep)"/>
        <stop offset="0.9" stop-color="#8fa3bd"/>
        <stop offset="1" stop-color="var(--cloud-white)"/>
      </radialGradient>
    </defs>
    <circle cx="900" cy="-480" r="812" fill="url(#earth-tones)"/>
  </svg>

  <h1 class="title">
    <span>A</span>
    <span>GARDEN</span>
    <span>LEFT</span>
    <span>STANDING</span>
  </h1>

  <p class="subtitle">A <strong>five-step plan to reverse climate change,</strong> to ensure that your grandchildren will live on a clean and comfortable planet.</p>

  <p class="author">MILO PARDREY</p>
</main>
</body>
</html>
```